develop our online residential property development appraisal service

This project requires a detailed WordPress design to represent a new digital residential property development consultancy business. At its heart it will have a number of different products that essentially advise customers of the potential value and feasibility of developing their residential site into multiple townhouses, units, apartments, etc... This will be accompanied by explaining the considerations of residential property development.

We aim to navigate and break down this complex area and provide our customers with the tools, knowledge, control and power to 'unlock the value' in their property.

REFERENCE DOCUMENTS:
1. Detailed solution requirements please refer to the attached 'wordpressdesignrequirements'
2. Logo files, style guide and colour pallet please refer to the attached 'KRMV.zip'
3. Site Map refer to attached 'wordpressdesignsitemap'

Reason: Additional information provided so extending period for designs to take into account.

Target Market(s)

The site will appeal to professional service providers; accountants, financial planners, lawyers, etc…

Industry/Entity Type

Residential

Font styles to use
Sans Serif
Other font styles liked:
• Similar to the logo font, slim line and simple

Requirements
Must have
• The logo, style and colour palette provided in the attached 'KRMV.zip' files
• Satisfy the intent of the 'wordpressdesignrequirements'
• Present as an online-centric business
• Clean, crisp and modern design
• Predominant use of white as a background contrasted with the colours provided in the colour palette
Nice to have
• Use of the following WordPress business themes is encouraged but not mandatory:
• 1. Tovu
• 2. Pilmu
• 3. Vomi
Should not have
• Overt references to Australia

```html
<!DOCTYPE html>
<html lang="en">
<head>
<meta charset="utf-8">
<title>KRMV – Keyline Residential Market Valuations</title>
<link rel="stylesheet" href="https://fonts.googleapis.com/css2?family=Open+Sans:wght@300;400;600;700&family=Roboto:wght@400;500;700&family=Roboto+Condensed:wght@400;700&display=swap">
<style>
  :root {
    --white: #ffffff;
    --ink: #222222;
    --text-grey: #555555;
    --soft-grey: #9a9a9a;
    --rule-grey: #8a8a8a;
    --brand-teal: #3f9c8c;
    --teal-overlay: rgba(58, 178, 160, 0.82);
    --green-b: #35a86a;
    --green-c: #5cbd45;
    --button-green: #3aa877;
    --button-lime: #63b84c;
    --button-teal: #2aa6a2;
    --bar-blue: #1e88d8;
    --bar-green: #4cbf5a;
    --footer-grey: #8c8c8c;
    --footer-dark: #5a5a5a;
  }
  * { margin: 0; padding: 0; box-sizing: border-box; }
  html, body { width: 1200px; height: 2300px; overflow: hidden; background: var(--white); }
  body { position: relative; font-family: "Open Sans", Arial, sans-serif; color: var(--ink); }
  .abs { position: absolute; }
  a { text-decoration: none; }

  /* Header */
  .brand { left: 54px; top: 56px; display: flex; align-items: center; }
  .brand-name { font-family: "Open Sans", sans-serif; font-weight: 300; font-size: 72px; line-height: 1; color: var(--brand-teal); letter-spacing: 1px; }
  .brand-divider { width: 2px; height: 80px; background: var(--rule-grey); margin: 0 14px 0 20px; }
  .brand-tagline { font-family: "Open Sans", sans-serif; font-weight: 300; font-size: 26px; line-height: 30px; color: #555; }
  .contact-link { left: 1050px; top: 126px; font-family: "Roboto", sans-serif; font-size: 18px; line-height: 22px; color: var(--ink); }
  .header-bar { left: 0; top: 168px; width: 1200px; height: 8px; background: linear-gradient(90deg, var(--bar-blue), var(--bar-green)); }

  /* Feature A */
  .photo { border-radius: 50%; }
  .feature-a-photo { left: 63px; top: 240px; width: 498px; height: 498px; background: radial-gradient(circle at 50% 30%, #cfd9e6 0%, #a9b4bc 45%, #6f7a72 100%); }
  .feature-a-badge { left: 153px; top: 332px; width: 307px; height: 307px; border-radius: 50%; background: var(--teal-overlay); display: flex; align-items: center; justify-content: center; text-align: center; color: var(--white); font-family: "Roboto", sans-serif; font-size: 28px; line-height: 36px; }
  .feature-a-text { left: 86px; top: 763px; width: 460px; text-align: center; white-space: nowrap; font-family: "Roboto", sans-serif; font-weight: 500; font-size: 27px; line-height: 41px; color: var(--soft-grey); }

  /* Report columns */
  .report-column { top: 192px; width: 282px; height: 1130px;
    background: linear-gradient(90deg, rgba(0,0,0,0.05) 0%, rgba(0,0,0,0) 6%, rgba(0,0,0,0) 94%, rgba(0,0,0,0.05) 100%);
    -webkit-mask-image: linear-gradient(180deg, transparent 0%, #000 12%, #000 85%, transparent 100%);
    mask-image: linear-gradient(180deg, transparent 0%, #000 12%, #000 85%, transparent 100%); }
  .column-b { left: 606px; }
  .column-c { left: 893px; }
  .report-badge { top: 218px; width: 117px; height: 117px; border-radius: 50%; display: flex; align-items: center; justify-content: center; text-align: center; color: var(--white); font-family: "Roboto", sans-serif; font-size: 15px; line-height: 19px; }
  .badge-b { left: 657px; background: var(--green-b); }
  .badge-c { left: 955px; background: var(--green-c); }
  .report-flow { top: 393px; display: flex; flex-direction: column; }
  .flow-b { left: 634px; width: 194px; }
  .flow-c { left: 928px; width: 222px; }
  .report-text { font-family: "Roboto Condensed", "Arial Narrow", sans-serif; font-weight: 700; font-size: 15.5px; line-height: 19.6px; color: #111; text-align: justify; hyphens: auto; -webkit-hyphens: auto; }
  .read-more { height: 24px; border-radius: 6px; color: var(--white); font-family: "Roboto", sans-serif; font-size: 11px; display: flex; align-items: center; justify-content: center; letter-spacing: 0.3px; }
  .more-b { width: 146px; margin: 33px 0 0 37px; background: var(--button-green); }
  .more-c { width: 148px; margin: 30px 0 0 31px; background: var(--button-lime); }
  .photo-b { width: 217px; height: 217px; margin-top: 19px; background: radial-gradient(circle at 50% 35%, #dfe6ee 0%, #9aa3a6 50%, #4e5650 100%); }
  .photo-c { width: 216px; height: 216px; margin-top: 21px; background: radial-gradient(circle at 50% 35%, #e4ecf4 0%, #a8b1b6 50%, #5c625e 100%); }

  /* About section */
  .blueprint { left: 300px; top: 1680px; width: 900px; height: 620px; background: radial-gradient(ellipse at 50% 70%, rgba(150,150,150,0.45) 0%, rgba(170,170,170,0.25) 45%, rgba(200,200,200,0) 72%); }
  .dotted-rule { left: 1183px; top: 1275px; height: 700px; border-left: 2px dotted #aaa; }
  .about-photo { top: 1357px; width: 307px; height: 307px; }
  .photo-who { left: 63px; background: radial-gradient(circle at 50% 40%, #c9ccd0 0%, #7c7f80 55%, #3c3e40 100%); }
  .photo-what { left: 441px; background: radial-gradient(circle at 50% 40%, #e2c84a 0%, #7a8fb0 55%, #3f5f8e 100%); }
  .photo-how { left: 815px; background: radial-gradient(circle at 50% 40%, #e8e8e8 0%, #b5b8bc 55%, #5c6066 100%); }
  .about-block { top: 1700px; width: 330px; }
  .about-who { left: 54px; }
  .about-what { left: 427px; }
  .about-how { left: 803px; }
  .about-block h2 { font-family: "Open Sans", sans-serif; font-weight: 700; font-size: 20px; line-height: 28px; color: var(--ink); margin-bottom: 22px; }
  .about-block p { font-family: "Open Sans", sans-serif; font-size: 17px; line-height: 23px; color: var(--text-grey); margin-bottom: 25px; }
  .more-about { top: 1986px; width: 138px; background: linear-gradient(90deg, #229a98, var(--button-teal)); }
  .more-who { left: 138px; }
  .more-what { left: 518px; }
  .more-how { left: 886px; }

  /* Footer */
  .site-footer { left: 0; top: 2065px; width: 1200px; height: 235px; background: var(--footer-grey); }
  .footer-base { left: 0; top: 2262px; width: 1200px; height: 38px; background: var(--footer-dark); }
  .footer-nav { left: 65px; top: 2132px; list-style: none; font-family: "Roboto", sans-serif; font-size: 16px; line-height: 20px; color: var(--white); }
  .copyright { left: 0; top: 2228px; width: 1200px; text-align: center; font-family: "Roboto", sans-serif; font-size: 11px; line-height: 14px; color: var(--white); }
  .social { left: 906px; top: 2218px; }
</style>
</head>
<body>

<header>
  <div class="abs brand">
    <span class="brand-name">KRMV</span>
    <span class="brand-divider"></span>
    <span class="brand-tagline">Keyline Residential<br>Market Valuations</span>
  </div>
  <a class="abs contact-link" href="#contact">Contact Us</a>
  <div class="abs header-bar"></div>
</header>

<main>
  <section class="feature-a">
    <div class="abs photo feature-a-photo" role="img" aria-label="Photo of a modern multi-storey apartment building with a parked car"></div>
    <div class="abs feature-a-badge">Property<br>Report<br>Page A</div>
    <p class="abs feature-a-text">Proin cursus quis mauris id<br>sollicitudin. Mauris et nulla<br>eget dolor dictum posuere<br>eget et lacus. Aenean conval-<br>lis felis sed ultricies semper.<br>Integer finibus egestas nisi, a<br>tempus elit lacinia eget.<br>Morbi tristique lacinia sagit-<br>tis. Nullam ut enim in odio<br>aliquam ultrices</p>
  </section>

  <div class="abs report-column column-b"></div>
  <div class="abs report-column column-c"></div>

  <section class="report-b">
    <div class="abs report-badge badge-b">Property<br>Report<br>Page B</div>
    <div class="abs report-flow flow-b">
      <p class="report-text">Contrary to popular belief, Lorem Ipsum is not simply random text. It has roots in a piece of classical Latin literature from 45 BC, making it over 2000 years old. Orin Masterly, a Latin professor at Brookvale-Hart College in Calder, looked up one of the more obscure Latin words, consectetur, from a Lorem Ipsum passage, and going through the cites of the word in classical literature, discovered the undoubtable source. Lorem Ipsum comes from sections 1.10.32 and 1.10.33 of "de Finibus Bonorum et Malorum" (The Extremes of Good and Evil) by Varro Lentus, written in 45 BC. This book is a treatise on the theory of ethics, very popular during the Renaissance. The first line of Lorem Ipsum, "Lorem ipsum dolor sit amet..", comes from a line in section 1.10.32.</p>
      <a class="read-more more-b" href="#report-b">READ MORE &gt;</a>
      <div class="photo photo-b" role="img" aria-label="Photo of a contemporary two-storey townhouse"></div>
    </div>
  </section>

  <section class="report-c">
    <div class="abs report-badge badge-c">Property<br>Report<br>Page C</div>
    <div class="abs report-flow flow-c">
      <p class="report-text">Lorem Ipsum is simply dummy text of the printing and typesetting industry. Lorem Ipsum has been the industry's standard dummy text ever since the 1500s, when an unknown printer took a galley of type and scrambled it to make a type specimen book. It has survived not only five centuries, but also the leap into electronic typesetting, remaining essentially unchanged. It was popularised in the 1960s with the release of Typeline sheets containing Lorem Ipsum passages, and more recently with desktop publishing software like Layflow Composer including versions of Lorem Ipsum.</p>
      <a class="read-more more-c" href="#report-c">READ MORE &gt;</a>
      <div class="photo photo-c" role="img" aria-label="Photo of a modern apartment block with balconies"></div>
    </div>
  </section>

  <section class="about">
    <div class="abs blueprint" role="img" aria-label="Faint architectural line drawing of a residential building"></div>
    <div class="abs dotted-rule"></div>

    <div class="abs photo about-photo photo-who" role="img" aria-label="Photo of a group of construction workers in hard hats"></div>
    <div class="abs photo about-photo photo-what" role="img" aria-label="Photo of a warehouse worker in a yellow hard hat"></div>
    <div class="abs photo about-photo photo-how" role="img" aria-label="Photo of colleagues talking at a meeting table"></div>

    <article class="abs about-block about-who">
      <h2>Who Are We ?</h2>
      <p>I'm a paragraph. Click here to add your own text and edit me. I'm a great place for you to tell a story and let your users know a little more about you.</p>
      <p>I'm a paragraph. Click here to add your own text and edit me. I'm a great place for you to tell a story and let your users know a little more about you.</p>
    </article>
    <article class="abs about-block about-what">
      <h2>What Do We Do ?</h2>
      <p>I'm a paragraph. Click here to add your own text and edit me. I'm a great place for you to tell a story and let your users know a little more about you.</p>
      <p>I'm a paragraph. Click here to add your own text and edit me. I'm a great place for you to tell a story and let your users know a little more about you.</p>
    </article>
    <article class="abs about-block about-how">
      <h2>How Do We Do It ?</h2>
      <p>I'm a paragraph. Click here to add your own text and edit me. I'm a great place for you to tell a story and let your users know a little more about you.</p>
      <p>I'm a paragraph. Click here to add your own text and edit me. I'm a great place for you to tell a story and let your users know a little more about you.</p>
    </article>

    <a class="abs read-more more-about more-who" href="#who">READ MORE &gt;</a>
    <a class="abs read-more more-about more-what" href="#what">READ MORE &gt;</a>
    <a class="abs read-more more-about more-how" href="#how">READ MORE &gt;</a>
  </section>
</main>

<footer id="contact">
  <div class="abs site-footer"></div>
  <div class="abs footer-base"></div>
  <ul class="abs footer-nav">
    <li>HOME</li>
    <li>About Us</li>
    <li>Site Map</li>
    <li>Contact Us</li>
  </ul>
  <p class="abs copyright">Copyrights 2015 - All Rights Reserved</p>
  <svg class="abs social" width="220" height="26" viewBox="0 0 220 26" aria-label="Social links">
    <circle cx="10" cy="13" r="9" fill="#ffffff"/>
    <circle cx="50" cy="13" r="9" fill="#ffffff"/>
    <circle cx="90" cy="13" r="9" fill="#ffffff"/>
    <circle cx="130" cy="13" r="9" fill="#ffffff"/>
    <circle cx="170" cy="13" r="9" fill="#ffffff"/>
    <circle cx="210" cy="13" r="9" fill="#ffffff"/>
  </svg>
</footer>

</body>
</html>
```